Dental Medical History Form - Content provided

Design a medical history form for a dental practice. Content is provided so all that is needed is the formatting to make it look great and easy to read.

"Patient Information" to include all information contained in top portion of the "Patient Medical History Form" docx file.

"Medical History" should follow the formatting and content of the "Exact Medical History" file as this is what the entry fields look like in our practice software and so we would like it to match.

1st page - Patient info, allergies, medications, antibiotics, joint replacement, pregnancy.

2nd page - Do you have, or have you had, any of the following? . . . . . . .

Target Market(s)

All ages but must be clear enough for elderly to read. Use as much space as possible to keep font size bigger yet keep to two pages

Industry/Entity Type

Dental

Font styles to use
Sans Serif

Requirements
Must have
• All content provided
• Our logo at the top (file provided)
• Century Gothic Font
• Limit to two pages

```html
<!DOCTYPE html>
<html lang="en">
<head>
<meta charset="utf-8">
<title>Harbourview Dental – Confidential Medical History</title>
<link href="https://fonts.googleapis.com/css2?family=Arimo:wght@400;700&display=swap" rel="stylesheet">
<style>
:root{
  --bg:#e6e7e9;
  --paper:#ffffff;
  --ink:#3c3c40;
  --band:#58585d;
  --band-text:#ffffff;
  --line:#8a8a8f;
}
*{box-sizing:border-box;margin:0;padding:0}
html,body{width:1200px;height:1200px;overflow:hidden}
body{background:var(--bg);font-family:"Arimo",sans-serif;color:var(--ink);position:relative}
.page{position:absolute;top:282px;width:490px;height:634px;background:var(--paper)}
.page-one{left:102px}
.page-two{left:609px}
.abs{position:absolute}
.t{font-size:7.5px;line-height:1;white-space:nowrap}
.box{position:absolute;border:1px solid var(--line);height:14px;background:#fff}
.cb{display:inline-block;width:6px;height:6px;border:0.8px solid var(--ink);margin-left:2px;vertical-align:0}
.rd{display:inline-block;width:6px;height:6px;border:0.8px solid var(--ink);border-radius:50%;margin-right:1px}
.brand{left:29px;top:318px;top:36px;font-size:16px;font-weight:400;color:var(--ink);line-height:1;white-space:nowrap}
.practice{right:29px;top:28px;text-align:right;font-size:7.5px;line-height:9.6px;font-style:normal}
.practice b{font-weight:700}
.band{position:absolute;background:var(--band);color:var(--band-text)}
.title-band{left:29px;top:80px;width:432px;height:17px;text-align:center;font-size:11px;font-weight:700;line-height:17px;letter-spacing:0.2px}
.spec-band{left:29px;top:418px;width:432px;height:16px;font-size:8px;line-height:16px;padding-left:8px;font-weight:400}
.q{font-weight:700}
.opts{display:flex;justify-content:space-between;width:432px}
.opts.small .t{font-size:6.8px}
.footer-note{right:29px;top:604px}
.col{position:absolute;top:42px;width:211px}
.col-a{left:29px}
.col-b{left:250px}
.sec{margin-top:4px}
.sec:first-child{margin-top:0}
.sec-head{background:var(--band);color:var(--band-text);height:13px;line-height:13px;font-size:7.5px;padding-left:8px;margin-bottom:1px}
.row{height:13.2px;display:flex;align-items:center;font-size:7.5px;white-space:nowrap}
.row .lbl{flex:1}
.row .yn{width:59px;text-align:left}
.thanks{left:0;width:490px;text-align:center;font-size:5.5px;font-style:italic}
</style>
</head>
<body>

<section class="page page-one">
  <div class="abs brand">Harbourview Dental</div>
  <address class="abs practice"><b>Harbourview Dental</b><br>3.05/118 Coastal Parade<br>Terrigal NSW 2260<br>(02) 4300 1234</address>

  <h1 class="band title-band">CONFIDENTIAL MEDICAL HISTORY</h1>

  <div class="abs t" style="left:29px;top:110px">Name:</div><div class="box" style="left:54px;top:107px;width:187px"></div>
  <div class="abs t" style="left:81px;top:129px">Title</div>
  <div class="abs t" style="left:122px;top:129px">First</div>
  <div class="abs t" style="left:166px;top:129px">Middle</div>
  <div class="abs t" style="left:214px;top:129px">Last</div>
  <div class="abs t" style="left:29px;top:143px">Address:</div><div class="box" style="left:63px;top:140px;width:178px"></div>
  <div class="abs t" style="left:29px;top:159px">DOB:</div><div class="box" style="left:50px;top:156px;width:191px"></div>
  <div class="abs t" style="left:29px;top:176px">Email Address:</div><div class="box" style="left:83px;top:173px;width:158px"></div>
  <div class="abs t" style="left:29px;top:193px">Phone Number(s):</div><div class="box" style="left:96px;top:190px;width:145px"></div>
  <div class="abs t" style="left:101px;top:212px">Mobile</div>
  <div class="abs t" style="left:157px;top:212px">Work</div>
  <div class="abs t" style="left:208px;top:212px">Home</div>
  <div class="abs t" style="left:29px;top:226px">Emergency Contact Person:</div><div class="box" style="left:130px;top:223px;width:111px"></div>
  <div class="abs t" style="left:29px;top:243px">Name:</div><div class="box" style="left:54px;top:240px;width:187px"></div>
  <div class="abs t" style="left:29px;top:260px">Relationship:</div><div class="box" style="left:77px;top:257px;width:164px"></div>
  <div class="abs t" style="left:29px;top:277px">Phone number:</div><div class="box" style="left:85px;top:274px;width:156px"></div>

  <div class="abs t q" style="left:252px;top:111px">General Practitioner:</div>
  <div class="abs t" style="left:252px;top:124px">Name:</div><div class="box" style="left:278px;top:120px;width:183px"></div>
  <div class="abs t" style="left:252px;top:140px">Practice Name:</div><div class="box" style="left:309px;top:137px;width:152px"></div>
  <div class="abs t" style="left:252px;top:157px">Phone Number:</div><div class="box" style="left:309px;top:154px;width:152px"></div>
  <div class="abs t" style="left:252px;top:178px">Do you have a health fund with dental cover? <span class="rd"></span>Yes <span class="rd"></span>No</div>
  <div class="abs t" style="left:252px;top:195px">If so, what is the name of the fund?</div><div class="box" style="left:378px;top:191px;width:83px"></div>
  <div class="abs t" style="left:252px;top:212px">Fund Number?</div><div class="box" style="left:309px;top:205px;width:37px"></div>
  <div class="abs t" style="left:252px;top:225px">Priority Number on card: 0 &nbsp;1 &nbsp;2 &nbsp;3 &nbsp;4 &nbsp;&nbsp;&nbsp;5</div>
  <div class="abs t" style="left:252px;top:242px">Occupation:</div><div class="box" style="left:296px;top:239px;width:165px"></div>
  <div class="abs t" style="left:252px;top:260px">Referred by:</div><div class="box" style="left:300px;top:257px;width:161px"></div>

  <div class="abs t q" style="left:29px;top:311px">Please indicate if you are allergic to any of the following <span class="cb" style="margin:0"></span>?</div>
  <div class="abs opts" style="left:29px;top:324px">
    <span class="t">Aspirin<span class="cb"></span></span><span class="t">Codeine<span class="cb"></span></span><span class="t">Penicillin<span class="cb"></span></span><span class="t">Sulfites<span class="cb"></span></span><span class="t">Latex<span class="cb"></span></span><span class="t">Local Anaesthetic<span class="cb"></span></span><span class="t">Lactose<span class="cb"></span></span><span class="t">Nickel<span class="cb"></span></span>
  </div>
  <div class="abs t" style="left:29px;top:342px">Other:</div><div class="box" style="left:54px;top:338px;width:407px"></div>

  <div class="abs t q" style="left:29px;top:365px">Are you currently taking, or have ever taken, any of the following medication<span class="cb" style="margin:0"></span>?</div>
  <div class="abs opts small" style="left:29px;top:379px">
    <span class="t">Asthma inhaler<span class="cb"></span></span><span class="t">Anti-epileptics<span class="cb"></span></span><span class="t">Anti-depressants<span class="cb"></span></span><span class="t">Blood Pressure<span class="cb"></span></span><span class="t">Blood Thinners<span class="cb"></span></span><span class="t">Bisphosphonates<span class="cb"></span></span>
  </div>
  <div class="abs opts small" style="left:29px;top:392px">
    <span class="t">Chemotherapy<span class="cb"></span></span><span class="t">Insulin<span class="cb"></span></span><span class="t">Immunosuppressants<span class="cb"></span></span><span class="t">Steroids<span class="cb"></span></span><span class="t">Oral Contraceptive<span class="cb"></span></span><span class="t">Other<span class="cb"></span></span>
  </div>

  <div class="band spec-band">Please specify medication name, dose, and frequency where possible:</div>
  <div class="box" style="left:29px;top:440px;width:143px"></div><div class="box" style="left:174px;top:440px;width:143px"></div><div class="box" style="left:319px;top:440px;width:142px"></div>
  <div class="box" style="left:29px;top:459px;width:143px"></div><div class="box" style="left:174px;top:459px;width:143px"></div><div class="box" style="left:319px;top:459px;width:142px"></div>
  <div class="box" style="left:29px;top:478px;width:143px"></div><div class="box" style="left:174px;top:478px;width:143px"></div><div class="box" style="left:319px;top:478px;width:142px"></div>

  <div class="abs t" style="left:29px;top:502px"><b>Do you require antibiotic cover?</b> &nbsp;&nbsp;&nbsp;&nbsp;&nbsp;&nbsp;Yes<span class="cb"></span> &nbsp;&nbsp;&nbsp;No<span class="cb"></span></div>
  <div class="abs t" style="left:29px;top:519px"><b>Have you had a joint replacement?</b> &nbsp;&nbsp;Yes<span class="cb"></span> &nbsp;&nbsp;&nbsp;No<span class="cb"></span></div>
  <div class="abs t q" style="left:29px;top:536px">Women:</div>
  <div class="abs t" style="left:29px;top:553px"><b>Are you pregnant?</b> Yes<span class="cb"></span> &nbsp;&nbsp;&nbsp;No<span class="cb"></span> &nbsp;&nbsp;&nbsp;Possible<span class="cb"></span> &nbsp;&nbsp;&nbsp;or &nbsp;&nbsp;&nbsp;Yes<span class="cb"></span> &nbsp;&nbsp;&nbsp;No<span class="cb"></span></div>

  <div class="abs t footer-note">Please Turnover</div>
</section>

<section class="page page-two">
  <div class="abs t q" style="left:29px;top:30px">Do you have, or have you had, any of the following?</div>

  <div class="col col-a">
    <div class="sec"><div class="sec-head">Dental</div>
      <div class="row"><span class="lbl">Acid Reflux</span><span class="yn">Yes<span class="cb"></span> No<span class="cb"></span></span></div>
      <div class="row"><span class="lbl">Bad Breath/Taste</span><span class="yn">Yes<span class="cb"></span> No<span class="cb"></span></span></div>
      <div class="row"><span class="lbl">Bleeding/Swollen/Sore Gums</span><span class="yn">Yes<span class="cb"></span> No<span class="cb"></span></span></div>
      <div class="row"><span class="lbl">Blisters/Ulcers in Mouth</span><span class="yn">Yes<span class="cb"></span> No<span class="cb"></span></span></div>
      <div class="row"><span class="lbl">Broken tooth/filling</span><span class="yn">Yes<span class="cb"></span> No<span class="cb"></span></span></div>
      <div class="row"><span class="lbl">Burning tongue</span><span class="yn">Yes<span class="cb"></span> No<span class="cb"></span></span></div>
      <div class="row"><span class="lbl">Dry mouth</span><span class="yn">Yes<span class="cb"></span> No<span class="cb"></span></span></div>
      <div class="row"><span class="lbl">Food collection between teeth</span><span class="yn">Yes<span class="cb"></span> No<span class="cb"></span></span></div>
      <div class="row"><span class="lbl">Grinding/clenching teeth (day/night)</span><span class="yn">Yes<span class="cb"></span> No<span class="cb"></span></span></div>
      <div class="row"><span class="lbl">Loose teeth</span><span class="yn">Yes<span class="cb"></span> No<span class="cb"></span></span></div>
      <div class="row"><span class="lbl">Crooked teeth</span><span class="yn">Yes<span class="cb"></span> No<span class="cb"></span></span></div>
      <div class="row"><span class="lbl">Discoloured teeth</span><span class="yn">Yes<span class="cb"></span> No<span class="cb"></span></span></div>
      <div class="row"><span class="lbl">Sensitivity to Hot/Cold</span><span class="yn">Yes<span class="cb"></span> No<span class="cb"></span></span></div>
      <div class="row"><span class="lbl">Tooth pain when chewing</span><span class="yn">Yes<span class="cb"></span> No<span class="cb"></span></span></div>
      <div class="row"><span class="lbl">Jaw pain/Fracture</span><span class="yn">Yes<span class="cb"></span> No<span class="cb"></span></span></div>
      <div class="row"><span class="lbl">Orthodontic treatment/history</span><span class="yn">Yes<span class="cb"></span> No<span class="cb"></span></span></div>
      <div class="row"><span class="lbl">Oral Cancer</span><span class="yn">Yes<span class="cb"></span> No<span class="cb"></span></span></div>
    </div>
    <div class="sec"><div class="sec-head">Diet/Lifestyle</div>
      <div class="row"><span class="lbl">Drink more than one glass alcohol per day</span><span class="yn">Yes<span class="cb"></span> No<span class="cb"></span></span></div>
      <div class="row"><span class="lbl">Smoking</span><span class="yn">Yes<span class="cb"></span> No<span class="cb"></span></span></div>
      <div class="row"><span class="lbl">Carbonated drinks</span><span class="yn">Yes<span class="cb"></span> No<span class="cb"></span></span></div>
      <div class="row"><span class="lbl">Sugary foods</span><span class="yn">Yes<span class="cb"></span> No<span class="cb"></span></span></div>
    </div>
    <div class="sec"><div class="sec-head">Blood</div>
      <div class="row"><span class="lbl">Anaemia</span><span class="yn">Yes<span class="cb"></span> No<span class="cb"></span></span></div>
      <div class="row"><span class="lbl">Blood clots</span><span class="yn">Yes<span class="cb"></span> No<span class="cb"></span></span></div>
      <div class="row"><span class="lbl">Leukemia</span><span class="yn">Yes<span class="cb"></span> No<span class="cb"></span></span></div>
      <div class="row"><span class="lbl">Low platelets</span><span class="yn">Yes<span class="cb"></span> No<span class="cb"></span></span></div>
      <div class="row"><span class="lbl">Lymphoma</span><span class="yn">Yes<span class="cb"></span> No<span class="cb"></span></span></div>
      <div class="row"><span class="lbl">Haemophelia</span><span class="yn">Yes<span class="cb"></span> No<span class="cb"></span></span></div>
    </div>
    <div class="sec"><div class="sec-head">Chest</div>
      <div class="row"><span class="lbl">Bronchitis</span><span class="yn">Yes<span class="cb"></span> No<span class="cb"></span></span></div>
      <div class="row"><span class="lbl">Cystic Fibrosis</span><span class="yn">Yes<span class="cb"></span> No<span class="cb"></span></span></div>
      <div class="row"><span class="lbl">Emphysema</span><span class="yn">Yes<span class="cb"></span> No<span class="cb"></span></span></div>
      <div class="row"><span class="lbl">Pneumonia</span><span class="yn">Yes<span class="cb"></span> No<span class="cb"></span></span></div>
    </div>
    <div class="sec"><div class="sec-head">Infectious Disease</div>
      <div class="row"><span class="lbl">Creutzfeldt-Jakob Disease</span><span class="yn">Yes<span class="cb"></span> No<span class="cb"></span></span></div>
      <div class="row"><span class="lbl">Hepatitis A,B,C,D</span><span class="yn">Yes<span class="cb"></span> No<span class="cb"></span></span></div>
    </div>
  </div>

  <div class="col col-b">
    <div class="sec">
      <div class="row"><span class="lbl">HIV/AIDS</span><span class="yn">Yes<span class="cb"></span> No<span class="cb"></span></span></div>
      <div class="row"><span class="lbl">Influenza</span><span class="yn">Yes<span class="cb"></span> No<span class="cb"></span></span></div>
      <div class="row"><span class="lbl">Shingles</span><span class="yn">Yes<span class="cb"></span> No<span class="cb"></span></span></div>
      <div class="row"><span class="lbl">Tuberculosis</span><span class="yn">Yes<span class="cb"></span> No<span class="cb"></span></span></div>
    </div>
    <div class="sec"><div class="sec-head">Heart</div>
      <div class="row"><span class="lbl">Angina</span><span class="yn">Yes<span class="cb"></span> No<span class="cb"></span></span></div>
      <div class="row"><span class="lbl">Atrial Fibrillation</span><span class="yn">Yes<span class="cb"></span> No<span class="cb"></span></span></div>
      <div class="row"><span class="lbl">Blood Pressure (High/Low)</span><span class="yn">Yes<span class="cb"></span> No<span class="cb"></span></span></div>
      <div class="row"><span class="lbl">Congenital Heart Disease</span><span class="yn">Yes<span class="cb"></span> No<span class="cb"></span></span></div>
      <div class="row"><span class="lbl">Heart attack</span><span class="yn">Yes<span class="cb"></span> No<span class="cb"></span></span></div>
      <div class="row"><span class="lbl">Heart murmur</span><span class="yn">Yes<span class="cb"></span> No<span class="cb"></span></span></div>
      <div class="row"><span class="lbl">Heart surgery</span><span class="yn">Yes<span class="cb"></span> No<span class="cb"></span></span></div>
      <div class="row"><span class="lbl">Heart valve replacement</span><span class="yn">Yes<span class="cb"></span> No<span class="cb"></span></span></div>
      <div class="row"><span class="lbl">Infective endocarditis</span><span class="yn">Yes<span class="cb"></span> No<span class="cb"></span></span></div>
      <div class="row"><span class="lbl">Rheumatic Heart Disease</span><span class="yn">Yes<span class="cb"></span> No<span class="cb"></span></span></div>
      <div class="row"><span class="lbl">Pacemaker</span><span class="yn">Yes<span class="cb"></span> No<span class="cb"></span></span></div>
      <div class="row"><span class="lbl">Stent</span><span class="yn">Yes<span class="cb"></span> No<span class="cb"></span></span></div>
    </div>
    <div class="sec"><div class="sec-head">Other</div>
      <div class="row"><span class="lbl">Anxiety/PTSD</span><span class="yn">Yes<span class="cb"></span> No<span class="cb"></span></span></div>
      <div class="row"><span class="lbl">Arthritis</span><span class="yn">Yes<span class="cb"></span> No<span class="cb"></span></span></div>
      <div class="row"><span class="lbl">Alzheimer's</span><span class="yn">Yes<span class="cb"></span> No<span class="cb"></span></span></div>
      <div class="row"><span class="lbl">Asthma</span><span class="yn">Yes<span class="cb"></span> No<span class="cb"></span></span></div>
      <div class="row"><span class="lbl">Anaphylaxis</span><span class="yn">Yes<span class="cb"></span> No<span class="cb"></span></span></div>
      <div class="row"><span class="lbl">Auto-immune disease</span><span class="yn">Yes<span class="cb"></span> No<span class="cb"></span></span></div>
      <div class="row"><span class="lbl">Coeliac</span><span class="yn">Yes<span class="cb"></span> No<span class="cb"></span></span></div>
      <div class="row"><span class="lbl">Depression</span><span class="yn">Yes<span class="cb"></span> No<span class="cb"></span></span></div>
      <div class="row"><span class="lbl">Diabetes</span><span class="yn">Yes<span class="cb"></span> No<span class="cb"></span></span></div>
      <div class="row"><span class="lbl">Epilepsy</span><span class="yn">Yes<span class="cb"></span> No<span class="cb"></span></span></div>
      <div class="row"><span class="lbl">Kidney Disease</span><span class="yn">Yes<span class="cb"></span> No<span class="cb"></span></span></div>
      <div class="row"><span class="lbl">Liver Disease</span><span class="yn">Yes<span class="cb"></span> No<span class="cb"></span></span></div>
      <div class="row"><span class="lbl">Osteoporosis</span><span class="yn">Yes<span class="cb"></span> No<span class="cb"></span></span></div>
      <div class="row"><span class="lbl">Parkinson's</span><span class="yn">Yes<span class="cb"></span> No<span class="cb"></span></span></div>
      <div class="row"><span class="lbl">Radiation to Head/Neck</span><span class="yn">Yes<span class="cb"></span> No<span class="cb"></span></span></div>
      <div class="row"><span class="lbl">Schizophrenia</span><span class="yn">Yes<span class="cb"></span> No<span class="cb"></span></span></div>
      <div class="row"><span class="lbl">Snoring</span><span class="yn">Yes<span class="cb"></span> No<span class="cb"></span></span></div>
      <div class="row"><span class="lbl">Sleep apnea</span><span class="yn">Yes<span class="cb"></span> No<span class="cb"></span></span></div>
      <div class="row"><span class="lbl">Stroke</span><span class="yn">Yes<span class="cb"></span> No<span class="cb"></span></span></div>
    </div>
  </div>

  <div class="abs t" style="left:250px;top:549px">Other:</div><div class="box" style="left:274px;top:545px;width:187px"></div>
  <div class="abs t" style="left:29px;top:569px">Signature:</div><div class="box" style="left:67px;top:565px;width:173px"></div>
  <div class="abs t" style="left:344px;top:569px">Date:</div><div class="box" style="left:366px;top:565px;width:95px"></div>
  <p class="abs thanks" style="top:586px">Thank you for the time to complete your medical history form.</p>
  <p class="abs thanks" style="top:597px">Oral health is linked to overall health and this comprehensive questionnaire will help us to provide you with optimal and safe care.</p>
</section>

</body>
</html>
```